Brochure about Gun Trusts

Cover Page: Image of a firearm collection or a lockbox with the title]
Headline: Protect Your Firearms Collection with a Gun Trust
Subheading: Ensure Your Legacy Remains Private and Your Wishes Are Respected
[Page 1: What is a Gun Trust?]
Definition: A legally recognized trust that allows you to collect, own, and transfer firearms, including those restricted by the NFA.
Quote: "A gun trust is a revocable trust created to hold ownership of a firearm..." - QMR
[Page 2: Benefits of a Gun Trust]
Avoid Probate: Keep your firearms out of the public probate process, maintaining your privacy.
Multi-Generational Ownership: Easily transfer ownership to beneficiaries without the need for a court proceeding.
Shared Responsibility: Allow others to legally possess and use the firearms held in the trust.
[Page 3: The Risks of Not Having a Gun Trust]
Inheritance Issues: Firearms may not be transferred as intended, potentially leading to legal complications.
Probate and Public Disclosure: Your firearms collection becomes a public record.
[Page 4: How to Set Up a Gun Trust]
Consult with an Attorney: A firearms trust attorney will create a trust that complies with all federal and state laws.
Assign a Trustee: Choose a trustee to manage the trust if you become incapacitated or pass away.
Transfer Ownership: Assign your firearms to the trust.
[Back Cover: Call to Action]
Headline: Protect Your Firearms Legacy
Contact Information: Address, Phone Number, Email, Website
Offer: Free Consultation to discuss your options

```html
<!DOCTYPE html>
<html lang="en">
<head>
<meta charset="UTF-8">
<title>Gun Trust Brochure Cover</title>
<link rel="stylesheet" href="https://fonts.googleapis.com/css2?family=Bebas+Neue&family=Oswald:wght@300;400&display=swap">
<style>
  :root {
    --navy: #2a3a4b;
    --navy-deep: #0f1a26;
    --teal: #2f6670;
    --teal-dark: #1e4a55;
    --white: #ffffff;
    --photo-light: #a7a5a1;
    --photo-mid: #7d7b78;
    --photo-dark: #3b3b3c;
    --page-bg: #f0e2c6;
  }
  * { margin: 0; padding: 0; box-sizing: border-box; }
  html, body {
    width: 800px;
    height: 1200px;
    overflow: hidden;
    background: var(--page-bg);
  }
  .cover {
    position: relative;
    width: 800px;
    height: 1200px;
    overflow: hidden;
    background: var(--navy);
  }
  .cover-photo {
    position: absolute;
    inset: 0;
    background:
      linear-gradient(90deg, rgba(0,0,0,0) 75%, var(--photo-dark) 88%),
      linear-gradient(180deg, var(--photo-mid) 0%, var(--photo-light) 55%, var(--photo-mid) 100%);
  }
  .cover-shapes {
    position: absolute;
    inset: 0;
  }
  .cover-title {
    position: absolute;
    top: 120px;
    right: 110px;
    text-align: right;
    font-family: 'Bebas Neue', 'Oswald', sans-serif;
    font-size: 92px;
    line-height: 0.86;
    color: var(--white);
    letter-spacing: 0.5px;
  }
  .title-markers {
    position: absolute;
    top: 150px;
    right: 58px;
    width: 30px;
    display: flex;
    flex-direction: column;
    gap: 10px;
  }
  .title-markers span {
    display: block;
    height: 90px;
    background: var(--teal);
  }
  .cover-subtitle {
    position: absolute;
    top: 470px;
    left: 250px;
    width: 480px;
    font-family: 'Oswald', sans-serif;
    font-weight: 300;
    font-size: 31px;
    line-height: 58px;
    color: var(--white);
    text-transform: uppercase;
  }
  .cover-footer-band {
    position: absolute;
    left: 0;
    right: 0;
    bottom: 0;
    height: 26px;
    background: var(--navy);
    border-top: 10px solid var(--teal);
  }
</style>
</head>
<body>
  <main class="cover">
    <div class="cover-photo" role="img" aria-label="Photograph of a lit display wall holding a collection of rifles and pistols with gold finishes on a grey pegboard"></div>

    <svg class="cover-shapes" width="800" height="1200" viewBox="0 0 800 1200" aria-hidden="true">
      <polygon points="0,0 800,0 800,260 420,760 0,560" fill="var(--navy)"/>
      <polygon points="420,0 800,0 800,230" fill="var(--navy-deep)"/>
      <polygon points="0,430 230,540 0,660" fill="var(--teal-dark)" opacity="0.55"/>
      <path d="M0,640 L70,610 Q120,600 120,650 L120,760 L0,820 Z" fill="var(--navy)"/>
    </svg>

    <h1 class="cover-title">Protect Your<br>Firearms<br>Collection With A<br>Gun Trust</h1>
    <div class="title-markers" aria-hidden="true"><span></span><span></span><span></span></div>

    <p class="cover-subtitle">Ensure your legacy remains<br>private and your wishes are<br>respected</p>

    <div class="cover-footer-band" aria-hidden="true"></div>
  </main>
</body>
</html>
```